Postcard Design

Name of the Company is : Tidewell Harbor Sport Fishing Charters Block Island RI
Name of the boat : Kelp Ora Vim
local Captain Darnell Okafor
pricing and booking : 738-615-2904
We specialize in:

Shark & Tuna Trips
Full or half day Inshore Bass & Bluefish
Half day bottom fishing for Fluke, Sea Bass & Scup
Inshore night fishing trips
Custom Combination Charters also available
Our crew provides:
A professional and accommodating experience
A very child friendly environment
A range of technique options for every style of trip
An immense knowledge of the waters.
Our Vessel:
Meets all NMRB safety requirement
Twin 250 Hp Voskard Turbo Diesels
All updated electronics
On the comfort side : we have a restroom, and a galley area with a table so you can enjoy your lunch.

Payments : We except; Cash , Check , Qr, Lb, Pz and Ot

I have attached the logo I would like to use . If possible I would like to use the banners on the logo with Company Name & number.

```html
<!DOCTYPE html>
<html lang="en">
<head>
<meta charset="utf-8">
<title>Tidewell Harbor Sport Fishing Charters – Postcard</title>
<link rel="stylesheet" href="https://fonts.googleapis.com/css2?family=Arimo:wght@400;700&family=Dancing+Script:wght@600&display=swap">
<style>
  :root {
    --stage: #1d4266;
    --ocean-deep: #0b4c9c;
    --ocean: #1c74cf;
    --foam: #ffffff;
    --navy: #123a7a;
    --label-yellow: #e6e23c;
    --mist: #d5e9f8;
    --ink: #1a3f78;
    --chip: #e9f1fa;
    --sans: "Arimo", Arial, sans-serif;
    --script: "Dancing Script", cursive;
  }
  * { box-sizing: border-box; margin: 0; padding: 0; }
  html, body { width: 1200px; height: 800px; overflow: hidden; }
  body { background: var(--stage); font-family: var(--sans); position: relative; }

  .postcard {
    position: absolute; top: 214px; width: 560px; height: 373px;
    border-radius: 3px; overflow: hidden;
    box-shadow: 0 6px 18px rgba(0,0,0,.35);
  }

  /* ---------- back (info side) ---------- */
  .postcard--back { left: 27px; background: linear-gradient(160deg, var(--foam) 0%, var(--mist) 100%); color: var(--ink); }
  .brand {
    position: absolute; display: flex; align-items: center; gap: 10px;
    color: var(--navy); font-weight: 700; font-size: 14px; line-height: 1.2;
  }
  .brand__mark { width: 34px; height: 34px; border-radius: 50%; background: var(--navy); flex: none; }
  .postcard--back .brand { top: 26px; left: 250px; width: 290px; }
  .booking { position: absolute; top: 92px; left: 34px; width: 200px; text-align: center; }
  .booking__prompt { font-size: 13px; }
  .booking__phone { font-size: 27px; font-weight: 700; margin-top: 2px; }
  .payments { position: absolute; top: 162px; left: 34px; width: 200px; text-align: center; }
  .payments__cash { font-size: 12px; margin-bottom: 8px; }
  .payments__cards { display: flex; justify-content: center; gap: 6px; }
  .payments__card {
    width: 40px; height: 26px; border-radius: 3px; background: var(--chip);
    border: 1px solid #b9cfe6; font-size: 12px; font-weight: 700;
    display: flex; align-items: center; justify-content: center; color: var(--ink);
  }
  .vessel { position: absolute; top: 110px; left: 262px; width: 270px; font-size: 12.5px; line-height: 1.3; }
  .vessel ul + ul { margin-top: 12px; }
  .tagline {
    position: absolute; left: 30px; right: 20px; bottom: 30px;
    font-family: var(--script); font-size: 25px; color: var(--ink); text-align: center;
  }

  /* ---------- front (blue side) ---------- */
  .postcard--front { left: 613px; background: linear-gradient(170deg, var(--ocean) 0%, var(--ocean-deep) 100%); color: var(--foam); }
  .front-wave { position: absolute; inset: 0; }
  .postcard--front .brand { top: 18px; left: 140px; width: 300px; }
  .front-columns { position: absolute; top: 110px; left: 0; right: 0; bottom: 0; display: flex; }
  .front-columns__details { width: 250px; padding: 0 16px 0 24px; text-align: center; }
  .front-columns__services { flex: 1; padding: 0 18px 0 20px; border-left: 1px solid rgba(255,255,255,.25); font-size: 12px; line-height: 1.3; }
  .detail__label { color: var(--label-yellow); font-size: 11.5px; margin-top: 10px; }
  .detail__label:first-child { margin-top: 0; }
  .detail__value { font-size: 25px; font-weight: 700; line-height: 1.15; }
  .services__heading { font-weight: 700; font-size: 13px; margin: 0 0 3px; text-align: center; }
  .services__heading + ul + .services__heading { margin-top: 10px; }

  .arrow-list { list-style: none; }
  .arrow-list li { position: relative; padding-left: 13px; }
  .arrow-list li::before { content: "➜"; position: absolute; left: 0; font-size: 9px; top: 2px; }
</style>
</head>
<body>

  <section class="postcard postcard--back" aria-label="Postcard back">
    <div class="brand"><span class="brand__mark"></span><span>Tidewell Harbor Sport Fishing Charters<br>(738) 615-2904</span></div>

    <div class="booking">
      <p class="booking__prompt">Book your experience today!</p>
      <p class="booking__phone">(738) 615-2904</p>
    </div>

    <div class="payments">
      <p class="payments__cash">Cash &amp; Checks</p>
      <div class="payments__cards">
        <span class="payments__card">Qr</span>
        <span class="payments__card">Pz</span>
        <span class="payments__card">Lb</span>
        <span class="payments__card">Ot</span>
      </div>
    </div>

    <div class="vessel">
      <ul class="arrow-list">
        <li>Our vessel meets all NMRB safety requirements</li>
        <li>Twin 250 Hp Voskard Turbo Diesels</li>
        <li>All updated electronics</li>
      </ul>
      <ul class="arrow-list">
        <li>We have a restroom and a galley area with a table so you can enjoy your lunch!</li>
      </ul>
    </div>

    <p class="tagline">A bad day fishing is better than a good day at work!</p>
  </section>

  <section class="postcard postcard--front" aria-label="Postcard front">
    <svg class="front-wave" width="560" height="373" viewBox="0 0 560 373" aria-hidden="true">
      <path d="M0 0 H560 V200 C520 150 500 110 440 100 C360 86 300 70 230 80 C150 92 70 70 0 40 Z" fill="var(--foam)"/>
      <path d="M0 40 C70 70 150 92 230 80 C300 70 360 86 440 100 C500 110 520 150 560 200" fill="none" stroke="#8fc6f2" stroke-width="3"/>
    </svg>

    <div class="brand"><span class="brand__mark"></span><span>Tidewell Harbor Sport Fishing Charters<br>(738) 615-2904</span></div>

    <div class="front-columns">
      <div class="front-columns__details">
        <p class="detail__label">Name of our boat:</p>
        <p class="detail__value">Kelp Ora Vim</p>
        <p class="detail__label">Local Captain</p>
        <p class="detail__value">Darnell Okafor</p>
        <p class="detail__label">Pricing &amp; Booking</p>
        <p class="detail__value">(738) 615-2904</p>
      </div>
      <div class="front-columns__services">
        <p class="services__heading">We specialize in:</p>
        <ul class="arrow-list">
          <li>Shark &amp; Tuna Trips</li>
          <li>Full or half day Inshore Bass &amp; Bluefish</li>
          <li>Half day bottom fishing for Fluke, Sea Bass &amp; Scup</li>
          <li>Inshore night fishing trips</li>
          <li>Custom Combination Charters available</li>
        </ul>
        <p class="services__heading">Our crew provides:</p>
        <ul class="arrow-list">
          <li>A professional and accommodating experience</li>
          <li>A very child friendly environment</li>
          <li>A range of technique options for every style of trip</li>
          <li>An immense knowledge of the waters</li>
        </ul>
      </div>
    </div>
  </section>

</body>
</html>
```